History Wall for Corporate Office

We are working on our corporate office wall to include a graphic with our history, and when we opened the schools and dance studios.
We are looking for a professional look, vibrant graphic, but clean and very clear to understand.
The wall is going up from floor 1 to floor 2. Please see photos attached as reference.
Measurements provided as well.
Do not include the master logo as part of this design, as the master logo it's placed in the wall right next to this one (photo as reference will show this).
Things to consider:
- We want to include photos of the schools/studio openings. Attached are the photos of each school opening.
- Follow brand guidelines
- Mainly using Master Color palette (blues and yellows) with touches of the other colors if needed
Here's the order of school/studio openings:
1968 Bright Path Hollowmere
1971 Bright Path Fernwick
1975 Bright Path Harlow
1976 The Bright Path Conservatory of Dance
1978 Bright Path Collegiate
1979 Bright Path Cobalt • Preschool & Elementary School
1980 Bright Path Las Brisas
1981 Bright Path Cedar Crest
1984 Bright Path Middle School
1989 Bright Path Dorsey
1990 Bright Path Whitford
2005 Bright Path Garnet
2008 Bright Path Schools 40th Anniversary
2015 NHMS Talbot Studio
2016 NHMS Aspen Hollow Studio
2017 NHMS Cedar Crest Studio
2018 Bright Path Schools 50th Anniversary
2021 Kinetic Leagues Coastline
2022 NHMS Cedar Crest Studio
2024 Bright Path Sutter Ridge
Fonts to be used: Fellix (main font) and Handsome (highlights-if needed)
Sending two graphic ideas as reference of the design direction we would like to have.

```html
<!DOCTYPE html>
<html lang="en">
<head>
<meta charset="utf-8">
<title>History Wall – Bright Path Schools</title>
<link rel="stylesheet" href="https://fonts.googleapis.com/css2?family=Baloo+2:wght@600;700;800&display=swap">
<style>
  :root {
    --paper: #ffffff;
    --frame: #8a8a8a;
    --band-yellow: #fcc31a;
    --year-blue: #2a6fb6;
    --rail-blue: #1d5c80;
    --stair-blue: #3d6f8f;
    --accent-red: #d0222a;
    --accent-darkred: #a5191f;
    --accent-green: #1aab6c;
    --accent-darkgreen: #176b4f;
    --accent-orange: #f47a20;
    --accent-blue: #2a74c0;
    --accent-pink: #d3419a;
    --ink: #111111;
    --doodle-grey: #d9d9d9;
  }
  html, body {
    margin: 0;
    padding: 0;
    overflow: hidden;
    background: var(--paper);
  }
  .history-wall {
    position: relative;
    width: 1200px;
    height: 1000px;
    overflow: hidden;
    background: var(--paper);
  }
  .history-wall svg { display: block; }
  .wall-frame { fill: none; stroke: var(--frame); stroke-width: 1; }
  .timeline-band { fill: none; stroke: var(--band-yellow); stroke-width: 34; stroke-linecap: round; stroke-linejoin: round; }
  .floor-rail { fill: none; stroke: var(--rail-blue); stroke-width: 12; stroke-linecap: round; stroke-linejoin: round; }
  .stair-step { fill: none; stroke: var(--stair-blue); stroke-width: 1; }
  .year-label {
    font-family: "Baloo 2", sans-serif;
    font-weight: 700;
    font-size: 15px;
    fill: var(--year-blue);
    text-anchor: middle;
  }
  .connector { fill: none; stroke: var(--ink); stroke-width: 2; stroke-dasharray: 6 4; }
  .medallion-back { stroke: var(--ink); stroke-width: 2; }
  .medallion-photo { fill: url(#photoTone); stroke: var(--ink); stroke-width: 2; }
  .medallion-mystery { fill: var(--accent-pink); stroke: var(--ink); stroke-width: 2; }
  .medallion-milestone { fill: var(--band-yellow); stroke: var(--ink); stroke-width: 2; }
  .mystery-mark {
    font-family: "Baloo 2", sans-serif;
    font-weight: 800;
    font-size: 36px;
    fill: #ffffff;
    text-anchor: middle;
  }
  .milestone-text {
    font-family: "Baloo 2", sans-serif;
    font-weight: 700;
    font-size: 11px;
    fill: var(--year-blue);
    text-anchor: middle;
  }
  .doodle { fill: var(--doodle-grey); }
  .doodle-blue { fill: #8fb8e0; }
  .doodle-yellow { fill: #f2c23a; }
  .doodle-orange { fill: #f28a2c; }
  .doodle-green { fill: #2bb39a; }
  .back-red { fill: var(--accent-red); }
  .back-darkred { fill: var(--accent-darkred); }
  .back-green { fill: var(--accent-green); }
  .back-darkgreen { fill: var(--accent-darkgreen); }
  .back-orange { fill: var(--accent-orange); }
  .back-blue { fill: var(--accent-blue); }
  .back-yellow { fill: var(--band-yellow); }
</style>
</head>
<body>
<main class="history-wall">
<svg width="1200" height="1000" viewBox="0 0 1200 1000" xmlns="http://www.w3.org/2000/svg" aria-label="Bright Path Schools history timeline">
  <defs>
    <linearGradient id="photoTone" x1="0" y1="0" x2="0" y2="1">
      <stop offset="0" stop-color="#b9c6cf"/>
      <stop offset="0.55" stop-color="#9fb3a0"/>
      <stop offset="1" stop-color="#5e7566"/>
    </linearGradient>
  </defs>

  <rect class="wall-frame" x="8.5" y="45.5" width="1183" height="888"/>

  <!-- staircase outline -->
  <g class="stairs">
    <rect class="stair-step" x="330" y="905" width="82" height="28"/>
    <rect class="stair-step" x="412" y="886" width="83" height="47"/>
    <rect class="stair-step" x="495" y="867" width="83" height="66"/>
    <rect class="stair-step" x="578" y="848" width="84" height="85"/>
    <rect class="stair-step" x="662" y="829" width="83" height="104"/>
    <rect class="stair-step" x="745" y="810" width="83" height="123"/>
    <rect class="stair-step" x="828" y="791" width="84" height="142"/>
    <rect class="stair-step" x="912" y="772" width="83" height="161"/>
    <rect class="stair-step" x="995" y="753" width="83" height="180"/>
    <rect class="stair-step" x="1078" y="734" width="113" height="199"/>
  </g>

  <path class="floor-rail" d="M215,722 L330,724 L1080,562 L1172,562"/>

  <!-- connectors -->
  <g class="connectors">
    <path class="connector" d="M330,455 V432"/>
    <path class="connector" d="M374,492 V598 L360,610"/>
    <path class="connector" d="M413,478 V336"/>
    <path class="connector" d="M455,497 V514 L442,524"/>
    <path class="connector" d="M496,452 V400 L510,388"/>
    <path class="connector" d="M537,442 V566"/>
    <path class="connector" d="M578,400 V300"/>
    <path class="connector" d="M620,428 V484"/>
    <path class="connector" d="M662,414 V350 L680,340"/>
    <path class="connector" d="M702,448 V535"/>
    <path class="connector" d="M745,412 V266 L756,258"/>
    <path class="connector" d="M783,424 V450"/>
    <path class="connector" d="M826,360 V300 L846,290"/>
    <path class="connector" d="M870,370 V496"/>
    <path class="connector" d="M922,350 V226"/>
    <path class="connector" d="M948,384 V408"/>
    <path class="connector" d="M990,370 V300 L1030,266"/>
    <path class="connector" d="M1032,388 V452"/>
    <path class="connector" d="M1075,336 V295 H1118 V184"/>
    <path class="connector" d="M1116,330 V372"/>
  </g>

  <path class="timeline-band" d="M320,468 C360,488 410,498 460,480 C510,462 540,420 600,414 C650,410 680,440 722,432 C770,424 800,392 830,375 C865,356 900,356 930,362 C970,372 1000,386 1040,374 C1080,362 1100,320 1138,305"/>

  <!-- years -->
  <g class="years">
    <text class="year-label" x="328" y="481">1968</text>
    <text class="year-label" x="372" y="492">1971</text>
    <text class="year-label" x="413" y="497">1975</text>
    <text class="year-label" x="454" y="492">1976</text>
    <text class="year-label" x="495" y="466">1978</text>
    <text class="year-label" x="536" y="435">1979</text>
    <text class="year-label" x="578" y="419">1980</text>
    <text class="year-label" x="620" y="419">1981</text>
    <text class="year-label" x="661" y="432">1984</text>
    <text class="year-label" x="703" y="440">1989</text>
    <text class="year-label" x="744" y="430">1990</text>
    <text class="year-label" x="784" y="412">2005</text>
    <text class="year-label" x="826" y="378">2008</text>
    <text class="year-label" x="868" y="362">2015</text>
    <text class="year-label" x="908" y="362">2016</text>
    <text class="year-label" x="950" y="372">2017</text>
    <text class="year-label" x="991" y="382">2018</text>
    <text class="year-label" x="1032" y="375">2021</text>
    <text class="year-label" x="1075" y="354">2022</text>
    <text class="year-label" x="1115" y="322">2024</text>
  </g>

  <!-- openings -->
  <g class="medallion"><circle class="medallion-back back-yellow" cx="360" cy="403" r="37"/><circle class="medallion-photo" cx="352" cy="395" r="37" role="img" aria-label="Opening photo of the Hollowmere school, 1968"/></g>
  <g class="medallion"><circle class="medallion-back back-orange" cx="358" cy="656" r="37"/><circle class="medallion-photo" cx="350" cy="648" r="37" role="img" aria-label="Opening photo of the Fernwick school, 1971"/></g>
  <g class="medallion"><circle class="medallion-back back-red" cx="438" cy="306" r="37"/><circle class="medallion-photo" cx="430" cy="298" r="37" role="img" aria-label="Opening photo of the Harlow school, 1975"/></g>
  <g class="medallion"><circle class="medallion-back back-darkgreen" cx="438" cy="571" r="37"/><circle class="medallion-mystery" cx="430" cy="563" r="37"/><text class="mystery-mark" x="430" y="576">???</text></g>
  <g class="medallion"><circle class="medallion-back back-blue" cx="536" cy="360" r="37"/><circle class="medallion-photo" cx="528" cy="352" r="37" role="img" aria-label="Opening photo of the Collegiate school, 1978"/></g>
  <g class="medallion"><circle class="medallion-back back-darkred" cx="536" cy="618" r="37"/><circle class="medallion-photo" cx="528" cy="610" r="37" role="img" aria-label="Opening photo of the Cobalt preschool and elementary school, 1979"/></g>
  <g class="medallion"><circle class="medallion-back back-green" cx="611" cy="270" r="37"/><circle class="medallion-photo" cx="603" cy="262" r="37" role="img" aria-label="Opening photo of the Las Brisas school, 1980"/></g>
  <g class="medallion"><circle class="medallion-back back-green" cx="613" cy="530" r="37"/><circle class="medallion-photo" cx="605" cy="522" r="37" role="img" aria-label="Opening photo of the Cedar Crest school, 1981"/></g>
  <g class="medallion"><circle class="medallion-back back-darkgreen" cx="713" cy="325" r="37"/><circle class="medallion-photo" cx="705" cy="317" r="37" role="img" aria-label="Opening photo of the middle school, 1984"/></g>
  <g class="medallion"><circle class="medallion-back back-yellow" cx="713" cy="580" r="37"/><circle class="medallion-photo" cx="705" cy="572" r="37" role="img" aria-label="Opening photo of the Dorsey school, 1989"/></g>
  <g class="medallion"><circle class="medallion-back back-darkgreen" cx="781" cy="238" r="37"/><circle class="medallion-photo" cx="773" cy="230" r="37" role="img" aria-label="Opening photo of the Whitford school, 1990"/></g>
  <g class="medallion"><circle class="medallion-back back-red" cx="781" cy="492" r="37"/><circle class="medallion-photo" cx="773" cy="484" r="37" role="img" aria-label="Opening photo of the Garnet school, 2005"/></g>
  <g class="medallion"><circle class="medallion-back back-blue" cx="888" cy="280" r="37"/><circle class="medallion-milestone" cx="880" cy="272" r="37"/>
    <text class="milestone-text" x="880" y="253">Bright Path</text><text class="milestone-text" x="880" y="265">Schools</text><text class="milestone-text" x="880" y="277">40th</text><text class="milestone-text" x="880" y="289">Anniversary</text></g>
  <g class="medallion"><circle class="medallion-back back-green" cx="888" cy="541" r="37"/><circle class="medallion-photo" cx="880" cy="533" r="37" role="img" aria-label="Opening photo of the Talbot dance studio, 2015"/></g>
  <g class="medallion"><circle class="medallion-back back-yellow" cx="953" cy="198" r="37"/><circle class="medallion-photo" cx="945" cy="190" r="37" role="img" aria-label="Opening photo of the Aspen Hollow dance studio, 2016"/></g>
  <g class="medallion"><circle class="medallion-back back-orange" cx="953" cy="453" r="37"/><circle class="medallion-photo" cx="945" cy="445" r="37" role="img" aria-label="Opening photo of the Cedar Crest dance studio, 2017"/></g>
  <g class="medallion"><circle class="medallion-back back-green" cx="1068" cy="240" r="37"/><circle class="medallion-milestone" cx="1060" cy="232" r="37"/>
    <text class="milestone-text" x="1060" y="213">Bright Path</text><text class="milestone-text" x="1060" y="225">Schools</text><text class="milestone-text" x="1060" y="237">50th</text><text class="milestone-text" x="1060" y="249">Anniversary</text></g>
  <g class="medallion"><circle class="medallion-back back-blue" cx="1068" cy="496" r="37"/><circle class="medallion-mystery" cx="1060" cy="488" r="37"/><text class="mystery-mark" x="1060" y="501">???</text></g>
  <g class="medallion"><circle class="medallion-back back-orange" cx="1128" cy="153" r="37"/><circle class="medallion-photo" cx="1120" cy="145" r="37" role="img" aria-label="Interior photo of the Cedar Crest dance studio, 2022"/></g>
  <g class="medallion"><circle class="medallion-back back-red" cx="1128" cy="416" r="37"/><circle class="medallion-photo" cx="1120" cy="408" r="37" role="img" aria-label="Opening photo of the Sutter Ridge school, 2024"/></g>

  <!-- activity doodles -->
  <rect class="doodle-blue" x="328" y="276" width="40" height="62" rx="12" role="img" aria-label="Doodle of a saxophone with music notes"/>
  <rect class="doodle-blue" x="424" y="358" width="40" height="66" rx="10" role="img" aria-label="Doodle of a telescope on a tripod"/>
  <rect class="doodle" x="474" y="190" width="60" height="88" rx="12" role="img" aria-label="Line doodle of a microscope"/>
  <rect class="doodle" x="603" y="318" width="40" height="58" rx="8" role="img" aria-label="Line doodle of a computer with play button"/>
  <rect class="doodle-yellow" x="566" y="445" width="42" height="24" rx="10" role="img" aria-label="Doodle of theatre masks"/>
  <rect class="doodle" x="590" y="578" width="70" height="40" rx="8" role="img" aria-label="Line doodle of a graduation cap"/>
  <ellipse class="doodle-green" cx="446" cy="648" rx="28" ry="24" role="img" aria-label="Doodle of a paint palette"/>
  <rect class="doodle-orange" x="764" y="282" width="38" height="60" rx="14" role="img" aria-label="Doodle of a basketball and hoop"/>
  <rect class="doodle" x="818" y="132" width="76" height="86" rx="14" role="img" aria-label="Line doodle of an astronaut with stars"/>
  <rect class="doodle-blue" x="810" y="418" width="40" height="42" rx="8" role="img" aria-label="Doodle of a presentation board"/>
  <rect class="doodle" x="950" y="502" width="40" height="50" rx="12" role="img" aria-label="Line doodle of a head with a brain"/>
</svg>
</main>
</body>
</html>
```